Structural Engineering Firm Looking for High-Impact Lead Generation Focused Design (for B2B)

A well-established structural engineering firm in the UK wants a new website designed for them which will help them realise more business from online. Directly through the website as well as Ads and lead platforms. They need to compare favourably to competitors and have clarity. Current Site is here: http://www.marlowgrantpartners.example/ - you can take imagery from this site if you want to help with the design.
Updates

Target Market(s)

Homeowners, Architects, Designers, Construction Companies and Landlords

Industry/Entity Type

Professional Services

Number of Pages Required

5+ page

Font styles to use
Sans Serif

Requirements
Must have
• A Strong, Simple and Professional Design with a Focus on Lead Generation
Nice to have
• Creativity in the Detail, Clear Messaging
Should not have
• Too Much Colour, Too 'Consumer', Too Much Variation

```html
<!DOCTYPE html>
<html lang="en">
<head>
<meta charset="utf-8">
<title>Marlow Grant Partners – Structural Engineering &amp; Party Wall Surveying</title>
<link href="https://fonts.googleapis.com/css2?family=Poppins:wght@400;500;600&display=swap" rel="stylesheet">
<style>
:root{
  --orange:#ea7a5b;
  --red:#d6474a;
  --teal:#a8c8bf;
  --beige:#e6dfcc;
  --plum:#4b4153;
  --ink:#1d1d20;
  --text:#2c2c30;
  --muted:#55555c;
  --footer:#1f1e23;
  --white:#ffffff;
}
*{box-sizing:border-box;margin:0;padding:0}
html,body{width:1200px;height:3636px;overflow:hidden}
body{font-family:"Poppins",Arial,sans-serif;color:var(--text);background:var(--white);position:relative}
.abs{position:absolute}
section,header,footer{position:absolute;left:0;width:1200px}

/* header */
.site-header{top:0;height:88px;background:var(--white)}
.top-bar{position:absolute;right:0;top:0;width:487px;height:30px;background:var(--orange);clip-path:polygon(16px 0,100% 0,100% 100%,0 100%);display:flex;align-items:center;padding-left:46px;gap:12px;font-size:11px;color:var(--white)}
.top-bar span.sep{opacity:.8}
.logo{position:absolute;left:215px;top:16px;font-size:27px;line-height:26px;font-weight:500;color:var(--ink);letter-spacing:-.5px}
.main-nav{position:absolute;top:51px;left:594px;display:flex;gap:37px;font-size:12px;font-weight:500;color:var(--ink)}
.main-nav .active{color:var(--orange)}

/* hero */
.hero{top:88px;height:474px;background:linear-gradient(180deg,#2f3a2c 0%,#46503f 35%,#6b5b48 60%,#8d7a62 80%,#4f5a3d 100%)}
.hero-title{position:absolute;top:145px;left:0;width:1200px;text-align:center;color:var(--white);font-size:31px;line-height:37px;font-weight:500}
.hero-sub{position:absolute;top:242px;width:1200px;text-align:center;color:var(--white);font-size:22px}
.select{position:absolute;background:var(--white);display:flex;align-items:center;justify-content:space-between;padding:0 12px;font-size:10px;color:var(--muted)}
.select svg{width:10px;height:6px}
.hero .select{left:407px;top:290px;width:387px;height:30px}

/* intro */
.intro{top:562px;height:558px}
.h2{font-size:22px;line-height:27px;font-weight:500;color:var(--ink)}
.body{font-size:10.5px;line-height:15px;color:var(--text)}
.art{position:absolute;border-radius:4px}

/* process */
.process-band{top:1120px;height:228px;background:var(--teal)}
.process{top:1120px;height:380px}
.btn-outline{position:absolute;border:1.5px solid var(--red);color:var(--red);font-size:12px;font-weight:500;display:flex;align-items:center;justify-content:center;background:transparent}
.step{position:absolute;top:139px;width:181px;height:219px}
.step .photo{height:181px}
.step .label{height:38px;display:flex;align-items:center;justify-content:center;color:var(--white);font-size:13px;font-weight:600}

/* turnaround */
.turnaround{top:1500px;height:427px}
.btn-solid{position:absolute;background:var(--red);color:var(--white);font-size:12px;font-weight:500;display:flex;align-items:center;justify-content:center}

/* partnership */
.partners{top:1927px;height:407px;background:linear-gradient(180deg,#3d3630 0%,#5a5048 45%,#6e665e 75%,#4e4740 100%);color:var(--white);text-align:center}
.partners h2{position:absolute;top:68px;width:1200px;font-size:31px;font-weight:500}
.partners p{position:absolute;width:1200px;font-size:12px;line-height:15px}
.btn-ghost{position:absolute;border:1.5px solid var(--white);color:var(--white);font-size:11.5px;font-weight:500;display:flex;align-items:center;justify-content:center}

/* news */
.news-band{top:2334px;height:272px;background:var(--beige)}
.news{top:2334px;height:400px}
.news h2,.locations h2{position:absolute;width:1200px;text-align:center;font-size:22px;font-weight:500;color:var(--ink)}
.card{position:absolute;top:116px;width:249px;height:275px;background:var(--white);box-shadow:0 2px 10px rgba(0,0,0,.08)}
.card .photo{height:156px}
.card .date{margin-top:20px;text-align:center;color:var(--red);font-size:12px}
.card .title{margin-top:12px;text-align:center;font-size:14.5px;line-height:22px;color:var(--ink)}

/* locations */
.locations{top:2734px;height:528px}
.tabs{position:absolute;left:407px;top:104px;width:387px;height:28px}
.tabs .rule{position:absolute;top:14px;left:0;width:387px;height:1px;background:var(--ink)}
.tab{position:absolute;top:0;height:28px;display:flex;align-items:center;justify-content:center;font-size:11.5px;font-weight:500}
.tab.on{left:100px;width:98px;background:var(--plum);color:var(--white)}
.tab.off{left:190px;width:96px;background:var(--white);border:1px solid var(--ink);color:var(--ink);clip-path:polygon(10px 0,100% 0,100% 100%,0 100%)}
.office{position:absolute;left:200px;font-size:13px;line-height:22px;color:var(--text)}
.office svg{width:13px;height:13px;vertical-align:-2px;margin-right:6px}

/* footer */
.site-footer{top:3262px;height:374px;background:var(--footer);color:var(--white)}
.f-logo{position:absolute;left:200px;top:66px;font-size:25px;line-height:24px;font-weight:500;color:var(--white)}
.f-col{position:absolute;top:78px;font-size:10px;line-height:22.5px;color:#e4e4e6}
.f-col h4{font-size:13px;font-weight:500;color:var(--orange);margin-bottom:6px;line-height:18px}
.f-contact{position:absolute;left:200px;top:140px;font-size:11px;line-height:22.5px}
.f-contact .city{color:#b9c5e6}
.social{position:absolute;top:266px;width:30px;height:30px;border:1.5px solid var(--red)}
.f-rule{position:absolute;left:200px;top:320px;width:800px;height:1px;background:#3a3940}
.f-bottom{position:absolute;top:340px;font-size:9.5px;color:#d8d8dc}
</style>
</head>
<body>

<header class="site-header">
  <div class="top-bar"><span>Gallery</span><span class="sep">|</span><span>Blog</span><span class="sep">|</span><span>About Us</span><span class="sep">|</span><span>Contact Us</span></div>
  <div class="logo">MARLOW GRANT<br>PARTNERS</div>
  <nav class="main-nav"><span class="active">Home</span><span>Engineering</span><span>Party Wall</span><span>Planning</span><span>Partners</span></nav>
</header>

<section class="hero" role="img" aria-label="Photograph of a modern timber and glass family house lit at dusk">
  <h1 class="hero-title">Efficient &amp; Professional Structural Engineering<br>&amp; Party Wall Surveying</h1>
  <p class="hero-sub">Get a competitive quote from the local experts</p>
  <div class="select"><span>What service are you looking for?</span><svg viewBox="0 0 10 6"><path d="M1 1l4 4 4-4" fill="none" stroke="#555" stroke-width="1.2"/></svg></div>
</section>

<section class="intro">
  <h2 class="h2 abs" style="left:200px;top:61px;width:400px">Structural engineers in london and the south east</h2>
  <p class="body abs" style="left:200px;top:127px;width:390px">If you're looking for structural engineering works in the South East, then you should talk to Marlow Grant Partners. Whether a basement, extension, 12ft or any other significant conversion to your home, we're here to help. Or perhaps you just want planning reports or advice on existing designs?</p>
  <p class="body abs" style="left:200px;top:203px;width:390px">Operating out of London and Sussex, we reach all the home counties and can provide you with a very quick appraisal and quote for the calculations and drawings.</p>
  <div class="art" style="left:654px;top:52px;width:278px;height:222px;background:radial-gradient(circle at 50% 55%,#e6f3dc 0%,#cfe6c2 45%,#f4f8f1 80%)" role="img" aria-label="Illustration of a smart house on a tablet surrounded by connected icons"></div>
  <div class="art" style="left:219px;top:320px;width:353px;height:156px;background:linear-gradient(90deg,#f3f1f8 0%,#c9c1ec 45%,#8f80d8 70%,#f3f1f8 100%)" role="img" aria-label="Illustration of people reviewing documents and finances beside a house"></div>
  <h2 class="h2 abs" style="left:611px;top:294px;width:400px">Choose the party wall specialists</h2>
  <p class="body abs" style="left:611px;top:335px;width:389px">Where there's a wall, there's a way. And we do more party wall awards than most surveyors. Whether it is part of a planning application, or serving or forming a party wall award, you can lean on us to help guide you through the process.</p>
  <p class="body abs" style="left:611px;top:410px;width:389px">Our experience makes us a very adaptable business to your needs. From minor residential works to major projects, we can work directly with you or be a part of your preferred design team.</p>
  <p class="body abs" style="left:611px;top:470px;width:389px">Simply call +44 (0) 1903 550218 for outside of London, or +44 (0) 20 7946 0417 within the capital, and we can get to work for you.</p>
</section>

<div class="process-band abs"></div>
<section class="process">
  <h2 class="h2 abs" style="left:200px;top:60px;width:420px">From drawing to delivered<br>we support you every step of the way</h2>
  <div class="btn-outline" style="left:875px;top:73px;width:125px;height:30px">Find Out More</div>
  <div class="step" style="left:200px"><div class="photo" style="background:linear-gradient(160deg,#d9b640,#8a6a3a 55%,#3d4a55)" role="img" aria-label="Photo of an engineer in hard hat on a building site"></div><div class="label" style="background:var(--ink)">Brief</div></div>
  <div class="step" style="left:407px"><div class="photo" style="background:linear-gradient(160deg,#9cb2c9,#d8d4cc 55%,#b08f72)" role="img" aria-label="Photo of a team working over architectural drawings"></div><div class="label" style="background:var(--orange)">Design</div></div>
  <div class="step" style="left:613px"><div class="photo" style="background:linear-gradient(160deg,#a9b7c6,#8b8f93 50%,#5d6e7e)" role="img" aria-label="Photo of a surveyor on a ladder checking a roof"></div><div class="label" style="background:var(--plum)">Refine</div></div>
  <div class="step" style="left:819px"><div class="photo" style="background:linear-gradient(160deg,#5c6f94,#8998b5 50%,#6b6f70)" role="img" aria-label="Photo of a couple outside their finished home"></div><div class="label" style="background:var(--red)">Deliver</div></div>
</section>

<section class="turnaround">
  <h2 class="h2 abs" style="left:200px;top:68px">Need a fast turnaround?</h2>
  <p class="body abs" style="left:200px;top:108px;width:390px">If your project is in the South East of England, we can provide a fast turnaround if needed. Simply tell us the scope of the work and provide an address and we can give you an indicative price and book a site visit.</p>
  <div class="select" style="left:200px;top:176px;width:281px;height:29px;border:1px solid #8a8a90"><span>What service are you looking for?</span><svg viewBox="0 0 10 6"><path d="M1 1l4 4 4-4" fill="none" stroke="#555" stroke-width="1.2"/></svg></div>
  <p class="body abs" style="left:200px;top:228px;width:390px">The Marlow Grant team will be on hand to help you through the process - from brief to calculations to delivery. Simply call: 01903550218 or book a site visit using our form.</p>
  <div class="btn-solid" style="left:200px;top:302px;width:125px;height:29px">Book a Site Visit</div>
  <div class="art" style="left:611px;top:40px;width:389px;height:325px;border-radius:0;background:linear-gradient(135deg,#b9b3aa 0%,#8b8276 40%,#4d6b85 70%,#c9c4bd 100%)" role="img" aria-label="Photo of a smiling man using his phone at a laptop"></div>
</section>

<section class="partners" role="img" aria-label="Photograph of a cobbled mews courtyard lined with white terraced houses">
  <h2>We work in partnership</h2>
  <p style="top:122px">We are familiar in working closely with architects, developers, builders and surveyors a wide range of projects.<br>So we are confident we can work with you.</p>
  <p style="top:170px;font-size:14px">if you would like to explore partnering with Marlow Grant:</p>
  <div class="btn-ghost" style="left:538px;top:209px;width:124px;height:29px">Partner With Us</div>
  <p style="top:260px;font-size:14px">if you would like to explore partnering with Marlow Grant:</p>
  <div class="btn-ghost" style="left:506px;top:300px;width:188px;height:29px">Introduce Us to Your Team</div>
</section>

<div class="news-band abs"></div>
<section class="news">
  <h2 style="top:59px">News, Event &amp; Features</h2>
  <div class="card" style="left:200px"><div class="photo" style="background:linear-gradient(135deg,#f2f2f0,#c8c9c4 60%,#3a3c3a)" role="img" aria-label="Photo of a bright modern kitchen interior"></div><div class="date">30-Jan-2022</div><div class="title">Lorem Ipsum is simply dummy<br>text of the printing</div></div>
  <div class="card" style="left:476px"><div class="photo" style="background:linear-gradient(180deg,#6fa7dc,#b8a08a 55%,#5b4a40)" role="img" aria-label="Photo of a modern brick town house"></div><div class="date">20-Feb-2022</div><div class="title">Lorem Ipsum is simply dummy<br>text of the printing</div></div>
  <div class="card" style="left:750px"><div class="photo" style="background:linear-gradient(90deg,#8d8d8b,#e9e7e2 45%,#b7c9a6 70%,#f0eeea)" role="img" aria-label="Photo of a bright living room opening onto a garden"></div><div class="date">10-Mar-2022</div><div class="title">Lorem Ipsum is simply dummy<br>text of the printing</div></div>
</section>

<section class="locations">
  <h2 style="top:48px">Our Locations</h2>
  <div class="tabs"><div class="rule"></div><div class="tab off">Sussex</div><div class="tab on">London</div></div>
  <h3 class="abs" style="left:200px;top:210px;font-size:17px;font-weight:500;color:var(--ink)">Marlow Grant Partners London</h3>
  <div class="office" style="top:256px;width:360px">
    <div><svg viewBox="0 0 14 14"><path d="M7 1a4 4 0 0 0-4 4c0 3 4 8 4 8s4-5 4-8a4 4 0 0 0-4-4zm0 5.5a1.5 1.5 0 1 1 0-3 1.5 1.5 0 0 1 0 3z" fill="none" stroke="#2c2c30" stroke-width="1"/></svg><b style="font-weight:500">Main Office:</b></div>
    <div style="padding-left:22px">Unit 4 Riverside Works, 22 Wharf Lane<br>London SW8 9ZX, United Kingdom</div>
    <div style="margin-top:14px"><svg viewBox="0 0 14 14"><path d="M3 1.5l2.3 2.4-1.2 1.6c.8 1.8 2.2 3.2 4 4l1.6-1.2 2.4 2.3-1.6 1.9C6 12 2 8 1.5 3.1z" fill="none" stroke="#2c2c30" stroke-width="1"/></svg>+44 (0) 20 7946 0417</div>
  </div>
  <div class="btn-outline" style="left:200px;top:400px;width:100px;height:29px">Contact Us</div>
  <div class="art" style="left:611px;top:165px;width:389px;height:301px;border-radius:0;background:linear-gradient(135deg,#eef0e6 0%,#cfe3c0 35%,#9fd0ef 50%,#eceee4 65%,#d2e6c4 100%)" role="img" aria-label="Street map of the south-west London office area with location pin"></div>
</section>

<footer class="site-footer">
  <div class="f-logo">MARLOW GRANT<br>PARTNERS</div>
  <div class="f-contact"><div class="city">London</div><div>+44 (0) 20 7946 0417</div><div class="city">Sussex</div><div>+44 (0) 1903 550218</div></div>
  <div class="social" style="left:200px"></div>
  <div class="social" style="left:238px;background:var(--red)"></div>
  <div class="social" style="left:276px"></div>
  <div class="f-col" style="left:406px"><h4>Engineering</h4>Basements<br>Lofts Conversion<br>Extensions<br>Structural Surveys<br>Temporary Works<br>Refurbishment &amp; Conversions<br>Commercial Projects<br>Structural Design Advice</div>
  <div class="f-col" style="left:612px"><h4>Party Wall</h4>Party Wall Notices<br>Party Wall Awards<br>Condition Schedules<br>Reviewing Engineer</div>
  <div class="f-col" style="left:818px;width:180px;line-height:11px"><h4>Planning</h4><div style="margin-bottom:11px">Structural Advise / Review</div><div style="margin-bottom:11px">Basement Construction Method Statements (CMS)</div><div style="margin-bottom:11px">Basement Impact Assessments (BIA)</div><div style="margin-bottom:11px">Basement Logistics Plan</div><div>Basement Construction Plan</div></div>
  <div class="f-rule"></div>
  <div class="f-bottom" style="left:200px">© 2022 Marlow Grant. All Rights Reserved.</div>
  <div class="f-bottom" style="left:612px;word-spacing:2px">Sitemap &nbsp;|&nbsp; Terms of Use &nbsp;|&nbsp; Privacy Policy &nbsp;|&nbsp; Contact Us</div>
</footer>

</body>
</html>
```